Web Design Project

The Varnholt Group is a strategy consulting group that works primarily with the healthcare industry. We provide a limited range of strategic planning & marketing services designed to focus on the growth and future viability of our clients’ organizations. We are a very small organization, but want to communicate a sense of boldness, forward-looking/visionary, and both creative and analytic. What follows below is: 1) A simple overview of the outline of the web-pages; 2) an important list of web-sites that appeal to me – the most important of which appears in a larger font; 3) photo ideas for the home page (from Pictavo.com). I have not written copy…and won’t until I know length based upon design.

The Varnholt Group
Healthcare Strategic Consulting

(Key Sections for the site)
HOME PAGE ABOUT US SERVICES NEWS & COMMENTS CONTACT US

(Sites That I Admire:)

http://www.lumenwirk.eu/services/ Very creative use of iconography to represent services, etc.

http://quillmoss.com/ Arresting graphics

http://brontiva.co/ GREAT SITE. THIS IS THE SITE THAT I LIKE THE MOST IN TERMS OF GENERAL LOOK & FEEL.

http://kasperholm.com/ Very interesting, stark/bold B&W site for architects

http://www.rtmalvey.com/ Interesting home page for promoting individual

HOME PAGE:

The Varnholt Group
STRATEGIC CONSULTING SERVICES (should be bold). We have a Logo that can be supplied later

Pictavo Image Options: 47193652, 36840157, 29617483, 58302619, 274815936, 61948237
Updates

Project Deadline Extended
Reason: The 1st and 2nd place designers will have an additional 5-7 days to complete the remaining pages of the site (approximately 11 pages). I have a file with all the photo information and rough copy that can be dropped into position.

Target Market(s)

Senior Executives (CEO,COO, CFO,SVP) in major hospitals or healthcare systems, other senior executives within healthcare.

Industry/Entity Type

Healthcare

Requirements
Must have
• I will want to pay to have this project expanded to show look and feel for:
*Home Page and key sections
*4 Pages that will be under the "About Us" heading
*5 Pages that will be under the "Services" heading

I have image options selected from Pictavo for all key sections. We will need to look at the cost for those images that the designer recommends.

```html
<!DOCTYPE html>
<html lang="en">
<head>
<meta charset="utf-8">
<title>The Varnholt Group — About Us</title>
<link rel="stylesheet" href="https://fonts.googleapis.com/css2?family=Marcellus&family=PT+Sans+Narrow:wght@400;700&family=PT+Sans:ital,wght@0,400;1,400&family=PT+Serif:ital@1&display=swap">
<style>
  :root {
    --header-dark: #27303c;
    --header-mid: #3f4a55;
    --white: #ffffff;
    --heading-grey: #8a9295;
    --text-grey: #5d6266;
    --rule: #e3e5e6;
    --rule-dark: #c9cccd;
    --btn-light-top: #a9b1b3;
    --btn-light-bottom: #7f888b;
    --btn-dark-top: #7b8083;
    --btn-dark-bottom: #4f5457;
    --video-bg: #1f2122;
    --icon-dark: #3c3f42;
    --photo-frame: #e6e8e8;
    --team-bg: #dcdcdc;
  }
  * { box-sizing: border-box; margin: 0; padding: 0; }
  html, body { width: 836px; height: 1200px; overflow: hidden; background: var(--white); }
  body { position: relative; font-family: "PT Sans", sans-serif; color: var(--text-grey); }
  .abs { position: absolute; }

  .site-header {
    position: absolute; left: 0; top: 0; width: 836px; height: 90px;
    background: linear-gradient(100deg, var(--header-dark) 0%, var(--header-mid) 45%, #55606a 70%, var(--header-dark) 100%);
  }
  .brand { position: absolute; left: 62px; top: 12px; font-family: "Marcellus", serif; color: var(--white); font-size: 38px; line-height: 1; letter-spacing: 0.3px; }
  .brand-rule { position: absolute; left: 62px; top: 58px; width: 258px; height: 1px; background: rgba(255,255,255,0.7); }
  .tagline { position: absolute; left: 210px; top: 64px; color: var(--white); font-size: 9.5px; }
  .main-nav { position: absolute; right: 62px; top: 36px; display: flex; font-size: 9.5px; color: var(--white); }
  .main-nav span { padding: 0 6px; }
  .main-nav .sep { padding: 0; }
  .main-nav .current { border-bottom: 2px solid var(--white); padding-bottom: 1px; margin: 0 6px; padding-left: 0; padding-right: 0; }
  .nav-rule { position: absolute; left: 430px; right: 62px; top: 58px; height: 1px; background: rgba(255,255,255,0.55); }

  .page-title { position: absolute; left: 0; width: 836px; top: 122px; text-align: center; font-family: "PT Sans Narrow", sans-serif; font-weight: 700; font-size: 44px; color: var(--heading-grey); letter-spacing: -0.5px; }
  .page-sub { position: absolute; left: 0; width: 836px; top: 184px; text-align: center; font-family: "PT Sans Narrow", sans-serif; font-weight: 700; font-size: 17px; color: var(--heading-grey); }

  .btn { position: absolute; top: 215px; width: 211px; height: 36px; display: flex; align-items: center; justify-content: center; gap: 16px; font-family: "PT Sans Narrow", sans-serif; font-weight: 700; font-size: 17px; color: var(--white); border: 1px solid #c8cccd; }
  .btn-login { left: 200px; background: linear-gradient(var(--btn-light-top), var(--btn-light-bottom)); }
  .btn-register { left: 421px; background: linear-gradient(var(--btn-dark-top), var(--btn-dark-bottom)); }

  .video { position: absolute; left: 200px; top: 268px; width: 432px; height: 219px; background: #000; padding: 5px; }
  .video-still { width: 100%; height: 100%; background: radial-gradient(ellipse at 55% 60%, #3a3c3d 0%, var(--video-bg) 70%); }
  .play { position: absolute; left: 192px; top: 92px; }

  .rule { position: absolute; height: 1px; background: linear-gradient(90deg, transparent, var(--rule-dark) 20%, var(--rule-dark) 80%, transparent); }

  .intro { position: absolute; left: 110px; top: 545px; width: 617px; font-size: 9px; line-height: 16px; text-align: justify; }
  .view-more-center { position: absolute; left: 359px; top: 624px; width: 80px; text-align: center; font-family: "PT Serif", serif; font-style: italic; font-size: 10px; color: #8b9092; }

  .feature-title { position: absolute; left: 109px; font-family: "PT Sans Narrow", sans-serif; font-weight: 700; font-size: 17px; color: var(--heading-grey); }
  .feature-photo { position: absolute; left: 110px; width: 256px; height: 137px; background: var(--photo-frame); padding: 5px; }
  .feature-photo div { width: 100%; height: 100%; }
  .photo-handshake { background: linear-gradient(180deg, #e9eeec 0%, #c7cecc 70%, #9ea7a5 100%); }
  .photo-crossroad { background: linear-gradient(180deg, #d77a6a 0%, #a5566f 40%, #253a7a 60%, #10204e 100%); }
  .feature-divider { position: absolute; left: 397px; width: 1px; background: var(--rule-dark); }
  .feature-arrow { position: absolute; left: 384px; }
  .feature-text { position: absolute; left: 424px; width: 303px; font-size: 9px; line-height: 16px; text-align: justify; }
  .feature-text p + p { margin-top: 6px; }
  .feature-more { position: absolute; left: 424px; font-size: 9.5px; color: #7c8184; display: flex; align-items: center; gap: 5px; }

  .team-label { position: absolute; left: 109px; top: 1117px; font-family: "PT Sans Narrow", sans-serif; font-weight: 700; font-size: 17px; color: var(--heading-grey); }
  .team-photo { position: absolute; top: 1086px; width: 95px; height: 86px; background: #f0f0f0; border: 1px solid #dadada; padding: 4px; }
  .team-photo div { width: 100%; height: 100%; background: var(--team-bg); }
</style>
</head>
<body>

<header class="site-header" role="img" aria-label="Header photo of yellow road signs with arrows against a dusky sky">
  <div class="brand">The Varnholt Group</div>
  <div class="brand-rule"></div>
  <div class="tagline">Healthcare Strategic Consulting</div>
  <nav class="main-nav">
    <span class="current">HOME</span><span class="sep">|</span>
    <span>ABOUT US</span><span class="sep">|</span>
    <span>SERVICES</span><span class="sep">|</span>
    <span>NEWS &amp; COMMENTS</span><span class="sep">|</span>
    <span>CONTACT US</span>
  </nav>
  <div class="nav-rule"></div>
</header>

<h1 class="page-title">ABOUT US</h1>
<p class="page-sub">Excepteur sint occaecat cupidatat non proident sunt inculpa le officia</p>

<a class="btn btn-login">MEMBER LOG IN
  <svg width="15" height="15" viewBox="0 0 16 16"><circle cx="8" cy="8" r="7" fill="#f3f4f4" stroke="#6d7477"/><path d="M6.5 5 L10.5 8 L6.5 11Z" fill="#555b5e"/></svg>
</a>
<a class="btn btn-register">REGISTER HERE
  <svg width="15" height="15" viewBox="0 0 16 16"><circle cx="8" cy="8" r="7" fill="#f3f4f4" stroke="#4a4e51"/><path d="M6.5 5 L10.5 8 L6.5 11Z" fill="#555b5e"/></svg>
</a>

<div class="video">
  <div class="video-still" role="img" aria-label="Dark video still of a stethoscope resting on a keyboard"></div>
  <svg class="play" width="49" height="34" viewBox="0 0 49 34">
    <rect x="0.5" y="0.5" width="48" height="33" rx="4" fill="#111" stroke="#555"/>
    <path d="M20 9 L32 17 L20 25Z" fill="#fff"/>
  </svg>
</div>

<div class="rule" style="left:110px; top:522px; width:620px;"></div>

<p class="intro">Sed ut perspiciatis unde omnis iste natus error sit voluptatem accusantium doloremque laudantium, totam rem aperiam, eaque ipsa quae ab illo inventore veritatis et quasi architecto beatae vitae dicta sunt explicabo. Nemo enim ipsam voluptatem quia voluptas sit aspernatur aut odit aut fugit, sed quia consequuntur magni dolores eos qui ratione voluptatem sequi nesciunt. Neque porro quisquam est, qui dolorem ipsum quia dolor sit amet, consectetur, adipisci velit, sed quia non numquam eius modi tempora incidunt ut labore et dolore magnam aliquam quaerat voluptatem.</p>

<div class="rule" style="left:110px; top:631px; width:248px;"></div>
<div class="view-more-center">View more</div>
<div class="rule" style="left:434px; top:631px; width:296px;"></div>

<!-- Feature one -->
<h2 class="feature-title" style="top:654px;">Suspendisse fermentum</h2>
<div class="feature-photo" style="top:692px;"><div class="photo-handshake" role="img" aria-label="Photo of two businessmen shaking hands before a whiteboard strategy sketch"></div></div>
<div class="feature-divider" style="top:658px; height:170px;"></div>
<svg class="feature-arrow" style="top:723px;" width="26" height="26" viewBox="0 0 26 26"><circle cx="13" cy="13" r="13" fill="var(--icon-dark)"/><path d="M7 13 H18 M14 9 L18 13 L14 17" stroke="#fff" stroke-width="2.2" fill="none"/></svg>
<div class="feature-text" style="top:660px;">
  <p>Sed ut perspiciatis unde omnis iste natus error sit voluptatem accusantium dolor emque laudantium, totam rem aperiam, eaque ipsa quae ab illo inventore veri tatis et quasi architecto beatae vitae dicta sunt explicabo.</p>
  <p>Nemo enim ipsam voluptatem quia voluptas sit aspernatur aut odit aut fugit, uia consequuntur magni dolores eos qui ratione voluptatem sequi nesciunt. Neque porro quisquam est, qui dolorem ipsum quia dolor sit amet, consectetur, adipisci velit, sed quia non numquam eius modi tempora incidunt ut labore. Curabitur mollis varius massa, eget commodo neque.</p>
</div>
<div class="feature-more" style="top:810px;">VIEW MORE <svg width="6" height="8" viewBox="0 0 6 8"><path d="M0 0 L6 4 L0 8Z" fill="#7c8184"/></svg></div>

<!-- Feature two -->
<h2 class="feature-title" style="top:866px;">Suspendisse fermentum</h2>
<div class="feature-photo" style="top:904px;"><div class="photo-crossroad" role="img" aria-label="Photo of a road forking at a yellow sign under a sunset sky"></div></div>
<div class="feature-divider" style="top:870px; height:170px;"></div>
<svg class="feature-arrow" style="top:935px;" width="26" height="26" viewBox="0 0 26 26"><circle cx="13" cy="13" r="13" fill="var(--icon-dark)"/><path d="M7 13 H18 M14 9 L18 13 L14 17" stroke="#fff" stroke-width="2.2" fill="none"/></svg>
<div class="feature-text" style="top:872px;">
  <p>Sed ut perspiciatis unde omnis iste natus error sit voluptatem accusantium dolor emque laudantium, totam rem aperiam, eaque ipsa quae ab illo inventore veri tatis et quasi architecto beatae vitae dicta sunt explicabo.</p>
  <p>Nemo enim ipsam voluptatem quia voluptas sit aspernatur aut odit aut fugit, uia consequuntur magni dolores eos qui ratione voluptatem sequi nesciunt. Neque porro quisquam est, qui dolorem ipsum quia dolor sit amet, consectetur, adipisci velit, sed quia non numquam eius modi tempora incidunt ut labore. Curabitur mollis varius massa, eget commodo neque.</p>
</div>
<div class="feature-more" style="top:1022px;">VIEW MORE <svg width="6" height="8" viewBox="0 0 6 8"><path d="M0 0 L6 4 L0 8Z" fill="#7c8184"/></svg></div>

<!-- Team -->
<div class="rule" style="left:110px; top:1075px; width:620px;"></div>
<h2 class="team-label">Our Team</h2>
<div class="team-photo" style="left:192px;"><div role="img" aria-label="Team member portrait placeholder"></div></div>
<div class="team-photo" style="left:302px;"><div role="img" aria-label="Team member portrait placeholder"></div></div>
<div class="team-photo" style="left:411px;"><div role="img" aria-label="Team member portrait placeholder"></div></div>
<div class="team-photo" style="left:521px;"><div role="img" aria-label="Team member portrait placeholder"></div></div>
<div class="team-photo" style="left:631px;"><div role="img" aria-label="Team member portrait placeholder"></div></div>
<div class="rule" style="left:110px; top:1186px; width:620px;"></div>

</body>
</html>
```